PLOVEN Business Card

Coastal Build Additions and Refits. I need a business card designed for this new high end renovation business. I would like the logo centered on the back side with the ABN (37 915 402 176) on the bottom right hand corner.

I would like the following information placed on the other side along with some customized pattern or design.

Derek Collwood
Director
Phone: 1300 480 957
Fax: (02) 8145 9021
Website: www.plovenbuilders.com.au
Email: d.collwood@plovenbuilders.com.au
PO Box 87,
Kelvinbrook NSW 2069

(FB Logo) PLOVEN - Coastal Build Additions and Refits

The final design should communicate professionalism and trust.

Back side background colour: white
Front side: Undecided

```html
<!DOCTYPE html>
<html lang="en">
<head>
<meta charset="utf-8">
<title>PLOVEN Business Card</title>
<link rel="stylesheet" href="https://fonts.googleapis.com/css2?family=Crimson+Pro:wght@400;600&display=swap">
<style>
  :root {
    --stage: #1c1c1c;
    --card: #ffffff;
    --ink: #333333;
    --brand-blue: #1f4e8c;
    --band: #353535;
    --band-line: #c9c9c9;
    --mark-grey: #d6d6d6;
    --band-text: #f2f2f2;
    --social-blue: #2d7fd0;
  }
  * { margin: 0; padding: 0; box-sizing: border-box; }
  html, body { width: 1000px; height: 1200px; overflow: hidden; }
  body {
    background: var(--stage);
    position: relative;
    font-family: "Crimson Pro", Georgia, serif;
    color: var(--ink);
  }
  .card {
    position: absolute;
    width: 723px;
    height: 423px;
    background: var(--card);
    overflow: hidden;
  }
  .card--front { left: 145px; top: 72px; }
  .card--back  { left: 139px; top: 637px; }

  .abs { position: absolute; white-space: nowrap; }

  /* Front */
  .holder { right: 34px; top: 52px; text-align: right; }
  .holder__name { font-size: 23px; letter-spacing: 0.5px; color: var(--brand-blue); line-height: 1.1; }
  .holder__role { font-size: 19px; color: var(--ink); line-height: 1.2; }

  .wordmark { left: 0; width: 100%; text-align: center; font-weight: 600; color: var(--ink); letter-spacing: 4px; line-height: 1; }
  .tagline { left: 0; width: 100%; text-align: center; color: var(--brand-blue); text-transform: uppercase; letter-spacing: 1px; line-height: 1; font-weight: 600; }

  .card--front .wordmark { top: 118px; font-size: 64px; }
  .card--front .tagline  { top: 190px; font-size: 16px; }

  .contact { font-size: 19px; display: flex; align-items: center; gap: 6px; line-height: 1; }
  .contact svg { width: 16px; height: 16px; fill: var(--brand-blue); flex: none; }
  .contact--left { right: 390px; flex-direction: row; }
  .contact--right { left: 392px; }
  .contact--r1 { top: 239px; }
  .contact--r2 { top: 268px; }

  .divider-mark { left: 347px; top: 247px; width: 30px; height: 30px; background: var(--mark-grey); }

  .band {
    left: 0; top: 316px; width: 100%; height: 107px;
    background: var(--band);
    border-top: 4px solid var(--band-line);
  }
  .social-mark { left: 47px; top: 317px; width: 56px; height: 56px; background: var(--social-blue); }
  .band__text { font-size: 17px; color: var(--band-text); line-height: 23px; }
  .band__page { left: 121px; top: 334px; }
  .band__post { right: 36px; top: 334px; text-align: right; }

  /* Back */
  .card--back .back-mark { left: 331px; top: 64px; width: 62px; height: 62px; background: var(--mark-grey); }
  .card--back .wordmark { top: 178px; font-size: 86px; }
  .card--back .tagline  { top: 273px; font-size: 23px; }
  .abn { left: 0; width: 100%; top: 308px; text-align: center; font-size: 20px; color: var(--ink); }
</style>
</head>
<body>

<section class="card card--front" aria-label="Business card front">
  <div class="abs holder">
    <div class="holder__name">DEREK COLLWOOD</div>
    <div class="holder__role">Director</div>
  </div>

  <div class="abs wordmark">PLOVEN</div>
  <div class="abs tagline">Coastal Build Additions &amp; Refits</div>

  <div class="abs contact contact--left contact--r1">
    <span>1300 480 957</span>
    <svg viewBox="0 0 24 24" aria-hidden="true"><path d="M6.6 10.8a15.1 15.1 0 0 0 6.6 6.6l2.2-2.2c.3-.3.7-.4 1-.2 1.1.4 2.3.6 3.6.6.6 0 1 .4 1 1V20c0 .6-.4 1-1 1A17 17 0 0 1 3 4c0-.6.4-1 1-1h3.5c.6 0 1 .4 1 1 0 1.3.2 2.5.6 3.6.1.3 0 .7-.2 1z"/></svg>
  </div>
  <div class="abs contact contact--left contact--r2">
    <span>www.plovenbuilders.com.au</span>
    <svg viewBox="0 0 24 24" aria-hidden="true"><path d="M12 2a10 10 0 1 0 0 20 10 10 0 0 0 0-20zm0 2c1 0 2.4 2 3 5H9c.6-3 2-5 3-5zM4.3 11h3.6a16 16 0 0 0 .3 3.5H4.8A8 8 0 0 1 4.3 11zm.5 5.5h3.7c.4 1.3.9 2.4 1.5 3.2a8 8 0 0 1-5.2-3.2zM8.7 9H5a8 8 0 0 1 4.7-4.7C9.3 5.6 8.9 7.2 8.7 9zm1.2 2h4.2a14 14 0 0 1-.3 3.5h-3.6a14 14 0 0 1-.3-3.5zm.6 5.5h3c-.4 1.8-1 3.5-1.5 3.5s-1.1-1.7-1.5-3.5zm4.3 3.2c.6-.8 1.1-1.9 1.5-3.2h3.7a8 8 0 0 1-5.2 3.2zm1.6-5.2a16 16 0 0 0 .3-3.5h3.6a8 8 0 0 1-.5 3.5zm.3-5.5c-.2-1.8-.6-3.4-1.1-4.7A8 8 0 0 1 19 9z"/></svg>
  </div>

  <div class="abs divider-mark" aria-hidden="true"></div>

  <div class="abs contact contact--right contact--r1">
    <svg viewBox="0 0 24 24" aria-hidden="true"><path d="M7 2h8v6H7zM4 9h16a2 2 0 0 1 2 2v8a2 2 0 0 1-2 2H4a2 2 0 0 1-2-2v-8a2 2 0 0 1 2-2zm2 3v2h5v-2zm0 4v2h12v-2z"/></svg>
    <span>(02) 8145 9021</span>
  </div>
  <div class="abs contact contact--right contact--r2">
    <svg viewBox="0 0 24 24" aria-hidden="true"><path d="M2 5h20v14H2zm2 2v.4l8 5.6 8-5.6V7zm0 2.8V17h16V9.8l-8 5.6z"/></svg>
    <span>d.collwood@plovenbuilders.com.au</span>
  </div>

  <div class="abs band" aria-hidden="true"></div>
  <div class="abs social-mark" aria-hidden="true"></div>
  <div class="abs band__text band__page">PLOVEN - Coastal Build<br>Additions and Refits</div>
  <div class="abs band__text band__post">PO Box 87,<br>Kelvinbrook NSW 2069</div>
</section>

<section class="card card--back" aria-label="Business card back">
  <div class="abs back-mark" aria-hidden="true"></div>
  <div class="abs wordmark">PLOVEN</div>
  <div class="abs tagline">Coastal Build Additions &amp; Refits</div>
  <div class="abs abn">ABN (37 915 402 176)</div>
</section>

</body>
</html>
```